New Turmel Business Card Design

We need a business card to match our new branding. The look should utilize the elements as attached here (Vector files & new exec overview are attached.) I really like 'organic' looking elements (e.g. an idea would be to have this printed on recycled paper stock). Thank you! Looking forward to seeing your designs.

Business

```html
<!DOCTYPE html>
<html lang="en">
<head>
<meta charset="utf-8">
<title>Turmel Business Card</title>
<link href="https://fonts.googleapis.com/css2?family=Questrial&display=swap" rel="stylesheet">
<style>
  :root {
    --navy: #0a1a35;
    --blue: #1274bd;
    --green: #8cc63f;
    --paper: #fbfbf9;
    --backdrop: #e4e4e2;
  }
  * { margin: 0; padding: 0; box-sizing: border-box; }
  html, body { width: 1200px; height: 1000px; overflow: hidden; }
  body {
    background: var(--backdrop);
    font-family: "Questrial", "Century Gothic", sans-serif;
    position: relative;
  }
  .card {
    position: absolute;
    width: 600px;
    height: 343px;
    overflow: hidden;
    box-shadow: 0 6px 14px rgba(0,0,0,0.25);
  }
  .card-back {
    left: 530px; top: 70px;
    background: var(--navy);
    text-align: center;
  }
  .card-back .brand {
    display: flex; align-items: center; justify-content: center; gap: 18px;
    margin-top: 92px;
  }
  .brand-dot {
    width: 34px; height: 34px; border-radius: 50%;
    background: var(--green);
    flex: none;
  }
  .card-back .brand-name {
    font-size: 92px; line-height: 1; color: var(--blue); letter-spacing: 1px;
  }
  .card-back .tagline {
    font-size: 26px; color: var(--green); margin-top: 8px;
  }
  .card-back .web {
    font-size: 20px; color: var(--blue); margin-top: 48px; letter-spacing: 0.5px;
  }
  .card-front {
    left: 70px; top: 570px;
    background: var(--paper);
  }
  .front-swoosh { position: absolute; left: 0; top: 0; width: 600px; height: 343px; }
  .front-content {
    position: absolute; left: 170px; right: 20px; top: 36px;
    text-align: center;
  }
  .card-front .brand {
    display: flex; align-items: center; justify-content: center; gap: 10px;
  }
  .card-front .brand-dot { width: 20px; height: 20px; }
  .card-front .brand-name { font-size: 54px; line-height: 1; color: var(--blue); }
  .person-name { font-size: 24px; color: var(--blue); margin-top: 30px; letter-spacing: 0.5px; }
  .person-title { font-size: 18px; color: var(--green); margin-top: 2px; }
  .contact { list-style: none; margin-top: 22px; font-size: 17px; line-height: 1.45; color: var(--blue); }
  .contact .label { color: var(--green); }
</style>
</head>
<body>
  <section class="card card-back">
    <div class="brand">
      <span class="brand-dot"></span>
      <span class="brand-name">Turmel</span>
    </div>
    <p class="tagline">Reach Past Launch Day</p>
    <p class="web">www.turmel.com</p>
  </section>

  <section class="card card-front">
    <svg class="front-swoosh" viewBox="0 0 600 343" aria-hidden="true">
      <path d="M0 0 H150 Q30 170 150 343 H0 Z" fill="var(--green)"/>
      <path d="M150 0 H215 Q95 170 150 343 Q30 170 150 0 Z" fill="var(--blue)"/>
    </svg>
    <div class="front-content">
      <div class="brand">
        <span class="brand-dot"></span>
        <span class="brand-name">Turmel</span>
      </div>
      <p class="person-name">YOUR NAME</p>
      <p class="person-title">Title</p>
      <ul class="contact">
        <li><span class="label">Phone:</span> 123 456 7890</li>
        <li><span class="label">Mobile:</span> 123 456 7890</li>
        <li><span class="label">Email:</span> yourname@turmel.com</li>
        <li><span class="label">Address:</span> Street No, Name of City, Country, NY 12345</li>
      </ul>
    </div>
  </section>
</body>
</html>
```